Business Card Design

I would like a new business card design for an accounting firm that specializes in resolving clients tax problems. I want the card to give the impression that we are not your typical stodgy accounting firm, but at the same time we will get the job done.
Industry/Entity Type
Business
Contact Information for Business Card
Dorian T Welsby
Certified Public Accountant
38-27 52nd Street
Sunnyside, NY 11287
Tel: (718) 555-0142
Fax: (888) 555-0199
e-mail: dtwthecpa@ledgerpost.com
website: harborfilingreliefexperts.com

```html
<!DOCTYPE html>
<html lang="en">
<head>
<meta charset="utf-8">
<title>Dorian T Welsby, CPA – Business Card</title>
<link rel="stylesheet" href="https://fonts.googleapis.com/css2?family=Source+Sans+3:wght@400;700&display=swap">
<style>
  :root {
    --bg: #ece9e4;
    --card: #ffffff;
    --navy: #0d4684;
    --gold: #e0b21c;
    --ink: #3a3a3a;
    --shadow: rgba(0,0,0,0.18);
  }
  * { margin: 0; padding: 0; box-sizing: border-box; }
  html, body { width: 1200px; height: 900px; overflow: hidden; }
  body {
    background: var(--bg);
    font-family: "Source Sans 3", "Myriad Pro", Arial, sans-serif;
    position: relative;
  }
  .card {
    position: absolute;
    width: 525px;
    height: 300px;
    background: var(--card);
    box-shadow: 0 6px 18px var(--shadow);
  }
  .card--front { left: 60px; top: 150px; }
  .card--back  { left: 615px; top: 440px; }

  .name-mark {
    position: absolute;
    display: flex;
    align-items: center;
    gap: 12px;
  }
  .card--front .name-mark { left: 50%; top: 50%; transform: translate(-50%, -50%); flex-direction: column; gap: 6px; }
  .card--back .name-mark { left: 30px; bottom: 34px; flex-direction: column; align-items: flex-start; gap: 6px; }
  .name-mark__row { display: flex; align-items: center; gap: 12px; }
  .name-mark__square { width: 16px; height: 16px; background: var(--navy); }
  .name-mark__name {
    color: var(--navy);
    font-weight: 700;
    font-size: 30px;
    letter-spacing: 2px;
    text-transform: uppercase;
    white-space: nowrap;
  }
  .title {
    color: var(--gold);
    font-weight: 700;
    font-size: 13px;
    letter-spacing: 2.5px;
    text-transform: uppercase;
  }

  .contact {
    position: absolute;
    left: 290px;
    top: 34px;
    color: var(--ink);
    font-size: 14px;
    line-height: 1.3;
  }
  .contact__address { margin-bottom: 18px; }
  .contact__list { list-style: none; }
  .contact__item { display: flex; align-items: center; gap: 8px; margin-bottom: 3px; white-space: nowrap; }
  .contact__icon { width: 12px; height: 12px; flex: none; fill: var(--navy); }
</style>
</head>
<body>
  <section class="card card--front" aria-label="Card front">
    <div class="name-mark">
      <div class="name-mark__row">
        <span class="name-mark__square"></span>
        <span class="name-mark__name">Dorian T Welsby</span>
      </div>
      <span class="title">Certified Public Accountant</span>
    </div>
  </section>

  <section class="card card--back" aria-label="Card back">
    <div class="contact">
      <p class="contact__address">38-27 52nd Street<br>Sunnyside, NY 11287</p>
      <ul class="contact__list">
        <li class="contact__item">
          <svg class="contact__icon" viewBox="0 0 12 12"><path d="M2.5 0.5l2 2.3-1.1 1.3c.7 1.5 2 2.8 3.5 3.5l1.3-1.1 2.3 2-1.3 2.2C5 10.6 1.4 7 .3 1.8z"/></svg>
          (718) 555-0142
        </li>
        <li class="contact__item">
          <svg class="contact__icon" viewBox="0 0 12 12"><rect x="3" y="0.5" width="6" height="3"/><rect x="0.5" y="4" width="11" height="6" rx="1"/><rect x="3" y="8" width="6" height="3.5" fill="#fff"/></svg>
          (888) 555-0199
        </li>
        <li class="contact__item">
          <svg class="contact__icon" viewBox="0 0 12 12"><rect x="0.5" y="2" width="11" height="8"/><path d="M0.5 2.5l5.5 4 5.5-4" stroke="#fff" fill="none"/></svg>
          dtwthecpa@ledgerpost.com
        </li>
        <li class="contact__item">
          <svg class="contact__icon" viewBox="0 0 12 12"><path d="M5 7l2-2M4.5 5.2L3 6.7a1.8 1.8 0 002.5 2.5L7 7.7M7.5 6.8L9 5.3A1.8 1.8 0 006.5 2.8L5 4.3" stroke="#0d4684" stroke-width="1.3" fill="none" stroke-linecap="round"/></svg>
          harborfilingreliefexperts.com
        </li>
      </ul>
    </div>
    <div class="name-mark">
      <div class="name-mark__row">
        <span class="name-mark__square"></span>
        <span class="name-mark__name">Dorian T Welsby</span>
      </div>
      <span class="title">Certified Public Accountant</span>
    </div>
  </section>
</body>
</html>
```